Billboard Design: Helicopter + Tampa/St. Pete Beach Composite (5 Variations)

We are looking for a skilled graphic designer to create five (5) high impact billboard designs using the provided helicopter photos and Tampa/St. Pete Beach background photos. The helicopter images were NOT taken over Tampa, so the designer must realistically composite the helicopter and Feet POV into the Tampa skyline scenes. The final images must look authentic, natural, and professionally blended, not like a cheap Photoshop cutout. These designs will be used for a real billboard advertising campaign, so realism and visual impact are essential.

***Google Link to download high-resolution photos:***
https://files.quorvex.net/share/7hTqpLmZ2aWcXe9RbNs4UdKy0VgF3jQ8?mode=view

Required Scenes (5 Total):
1. Tampa Skyline + Helicopter Front
2. Tampa Skyline + Helicopter Side Door (facing backwards)
3. Tampa Skyline + Feet POV
4. Beach Background + Helicopter Front (You can use the Beach/Helicopter picture as provided since that photo was taken in the correct scene)
5. Beach Background + Helicopter Front (You can use the Beach/Helicopter picture as provided since that photo was taken in the correct scene)
Some designs must include the feet outside POV image.

Each Billboard Must Include:
• One catch phrase (assigned below)
• One discount phrase + discount code
• Our logo
• Our website: www.skyMARLO.com
• A realistic composite of:
o Helicopter
o Leg out POV
o Beach background

Catch Phrase + Discount Code Assignments:
1. Adventure Starts Here.
Use Code TAMPA25 for $25 Off

2. See Tampa From Above.
Take $25 Off with Code UP25

3. Elevate Your Weekend.
Use Code YES25 for $25 Off

4. The Ultimate Date Night.
Take $25 Off with Code LOVE25

5. Sunset Hits Different.
Use Code SUNSET25 for $25 Off

6. Premium Views. No Filter.
Take $25 Off with Code SKY25

7. Bucket List? Check.

(You will design five billboards, but these seven options are provided so you can choose the strongest matches for each scene.)

Deliverables:
• Five (5) billboard ready designs
• High resolution JPEG files in the exact required pixel dimensions
• Layered PSD files for future edits
• Consistent branding across all designs

Important Notes:
• The helicopter must look like it belongs in the scene. Correct lighting, shadows, and scale are essential.
• Designs should feel premium, exciting, and tourism oriented.
• This project is for a real billboard campaign, so quality must be top tier.

Billboard Specifications:
(IMPORTANT — MUST FOLLOW EXACTLY)
Your final artwork must match the exact pixel dimensions required by the billboard units. These are absolute pixel sizes and must be delivered 1:1 — no scaling, no DPI adjustments.

Billboard Size Option 1: 14' x 48' Digital Bulletin
• Display Resolution: 208 px (height) × 720 px (width)
• Mechanical/Artwork Size: 208 px × 720 px
• File Format: JPEG
• Color Mode: sRGB
• Bright white backgrounds are discouraged; if used, target R235 / G235 / B235 (“broadcast safe white”).
• File must be delivered at exact resolution (1:1 pixel ratio).

Billboard Size Option 2: 10'6" x 36' Digital Bulletin
• Display Resolution: 160 px (height) × 544 px (width)
• Mechanical/Artwork Size: 160 px × 544 px
• File Format: JPEG
• Color Mode: sRGB
• Same broadcast safe white recommendation applies.
• Must be delivered at exact resolution (1:1 pixel ratio).
Designers may create layouts for either size, but the final deliverables must be exported in the correct pixel dimensions for the selected unit.

Target Market(s)

Our billboards are aimed at tourists, couples, families, and locals looking for memorable experiences in Tampa and St. Pete. The audience includes visitors seeking unique aerial views, couples planning romantic outings, adventure‑seekers wanting something exciting and scenic, and social‑media‑driven customers who value visually striking, Instagram‑worthy moments.

Requirements
Must have
• The final designs must include photorealistic compositing of our helicopter into Tampa skyline or beach backgrounds, with lighting, shadows, and scale that look completely authentic. Designers must deliver artwork in the exact required pixel dimensions for the billboard units, using clean, bold typography that remains readable from a distance. Each design must include a catch phrase, a discount phrase with its code, our logo, and our website URL, and all files must be delivered as layered PSDs along with high‑resolution JPEGs.
Nice to have
• It is helpful if designers incorporate subtle atmospheric effects such as haze, color grading, or lighting adjustments to enhance realism and mood. Creative depth, perspective, or motion can make the helicopter feel more dynamic, and slight variations in tone or style across the five designs are welcome. Including the feet‑out POV image where it naturally fits the composition is also a plus.

```html
<!DOCTYPE html>
<html lang="en">
<head>
<meta charset="utf-8">
<title>SkyMarlo Billboard Series</title>
<link href="https://fonts.googleapis.com/css2?family=Oswald:wght@600;700&family=Poppins:wght@400;500;600&display=swap" rel="stylesheet">
<style>
:root{
  --blue:#1b5fe3;
  --blue-deep:#1449b8;
  --ink:#26272c;
  --white:#ffffff;
  --canvas:#3b3b3d;
  --stage:#2f2f31;
  --sky-warm:#e9a15a;
  --sky-cool:#6d8fb0;
  --city:#6b6f78;
  --sea:#2fb9b3;
}
*{box-sizing:border-box;margin:0;padding:0}
html,body{width:1200px;height:2637px;overflow:hidden;background:var(--canvas)}
body{position:relative;font-family:"Poppins",sans-serif}
.stage{position:absolute;left:0;top:0;width:1200px;height:698px;background:var(--stage)}
.hero-board{position:absolute;left:150px;top:218px;transform:scale(.841);transform-origin:0 0}
.board{position:absolute;left:65px;width:1070px;height:309px;background:var(--white);overflow:hidden}
.board svg.shapes{position:absolute;left:0;top:0;width:1070px;height:309px}
.headline{position:absolute;font-family:"Oswald",sans-serif;font-weight:700;color:var(--ink);line-height:1;letter-spacing:-.5px}
.offer{position:absolute;color:var(--white);font-family:"Poppins",sans-serif;font-weight:500;white-space:nowrap}
.offer b{font-family:"Oswald",sans-serif;font-weight:700;letter-spacing:-.3px}
.brand{position:absolute;display:flex;align-items:center;gap:8px;font-family:"Poppins",sans-serif;font-weight:600;font-size:22px;color:var(--blue)}
.brand i{display:block;width:16px;height:16px;border-radius:50%;background:var(--blue)}
.site{position:absolute;display:flex;align-items:center;gap:10px;height:34px;padding:0 18px 0 10px;border-radius:17px;background:var(--ink);color:var(--white);font-size:19px;font-weight:500;white-space:nowrap}
.site svg{width:24px;height:24px}
.site.blue{background:var(--blue);border-radius:17px 0 0 17px}
</style>
</head>
<body>

<svg width="0" height="0" style="position:absolute">
  <defs>
    <linearGradient id="dusk" x1="0" y1="0" x2="0" y2="1">
      <stop offset="0" stop-color="#7f9bb8"/><stop offset=".35" stop-color="#e7a866"/><stop offset=".55" stop-color="#8c8a88"/><stop offset="1" stop-color="#4d5563"/>
    </linearGradient>
    <linearGradient id="day" x1="0" y1="0" x2="0" y2="1">
      <stop offset="0" stop-color="#9fb8cf"/><stop offset=".4" stop-color="#c9bda6"/><stop offset="1" stop-color="#6a7380"/>
    </linearGradient>
    <linearGradient id="beach" x1="0" y1="0" x2="1" y2="0">
      <stop offset="0" stop-color="#37c6bd"/><stop offset=".45" stop-color="#7fd6c8"/><stop offset=".55" stop-color="#e8e3cf"/><stop offset="1" stop-color="#4f7a45"/>
    </linearGradient>
    <linearGradient id="sunset" x1="0" y1="0" x2="0" y2="1">
      <stop offset="0" stop-color="#3a4660"/><stop offset=".3" stop-color="#f09a3e"/><stop offset=".5" stop-color="#a26a4c"/><stop offset="1" stop-color="#3f4451"/>
    </linearGradient>
    <symbol id="globe" viewBox="0 0 24 24"><circle cx="12" cy="12" r="10" fill="none" stroke="#fff" stroke-width="1.6"/><ellipse cx="12" cy="12" rx="4.5" ry="10" fill="none" stroke="#fff" stroke-width="1.4"/><path d="M2 12h20M4 7h16M4 17h16" stroke="#fff" stroke-width="1.4"/></symbol>
  </defs>
</svg>

<div class="stage"></div>

<!-- Board template: Adventure -->
<div class="hero-board">
  <div class="board" style="left:0;top:0">
    <svg class="shapes" viewBox="0 0 1070 309">
      <path d="M600 0H1070V309H560C470 260 480 150 600 120Z" fill="var(--ink)"/>
      <path d="M630 0H1070V309H610C520 250 540 160 640 130Z" fill="var(--blue)"/>
      <path d="M670 0H1070V309H640C560 250 580 170 690 140C720 135 700 60 670 0Z" fill="url(#dusk)" role="img" aria-label="Helicopter flying over downtown Tampa at golden hour"/>
      <rect x="220" y="14" width="410" height="4" fill="var(--blue)"/>
      <path d="M0 18H640A50 50 0 0 1 640 118H0Z" fill="var(--white)"/>
    </svg>
    <div class="headline" style="left:34px;top:30px;font-size:70px">Adventure Starts Here</div>
    <svg class="shapes" viewBox="0 0 1070 309"><path d="M50 110H500V168H50A29 29 0 0 1 50 110Z" fill="var(--blue)"/></svg>
    <div class="offer" style="left:75px;top:118px;font-size:22px">Use Code <b style="font-size:38px">TAMPA25</b> for <b style="font-size:38px">$25</b> Off</div>
    <div class="brand" style="left:34px;top:240px"><i></i>SkyMarlo</div>
    <div class="site" style="left:255px;top:235px"><svg><use href="#globe"/></svg>www.skyMARLO.com</div>
  </div>
</div>

<div class="board" style="top:778px">
  <svg class="shapes" viewBox="0 0 1070 309">
    <path d="M600 0H1070V309H560C470 260 480 150 600 120Z" fill="var(--ink)"/>
    <path d="M630 0H1070V309H610C520 250 540 160 640 130Z" fill="var(--blue)"/>
    <path d="M670 0H1070V309H640C560 250 580 170 690 140C720 135 700 60 670 0Z" fill="url(#dusk)" role="img" aria-label="Helicopter flying over downtown Tampa at golden hour"/>
    <rect x="220" y="14" width="410" height="4" fill="var(--blue)"/>
    <path d="M0 18H640A50 50 0 0 1 640 118H0Z" fill="var(--white)"/>
  </svg>
  <div class="headline" style="left:34px;top:30px;font-size:70px">Adventure Starts Here</div>
  <svg class="shapes" viewBox="0 0 1070 309"><path d="M50 110H500V168H50A29 29 0 0 1 50 110Z" fill="var(--blue)"/></svg>
  <div class="offer" style="left:75px;top:118px;font-size:22px">Use Code <b style="font-size:38px">TAMPA25</b> for <b style="font-size:38px">$25</b> Off</div>
  <div class="brand" style="left:34px;top:240px"><i></i>SkyMarlo</div>
  <div class="site" style="left:255px;top:235px"><svg><use href="#globe"/></svg>www.skyMARLO.com</div>
</div>

<!-- See Tampa -->
<div class="board" style="top:1147px">
  <svg class="shapes" viewBox="0 0 1070 309">
    <path d="M0 0H430C560 20 570 250 400 309H0Z" fill="var(--blue)"/>
    <path d="M0 0H410C530 30 540 240 380 309H0Z" fill="url(#dusk)" role="img" aria-label="View of Tampa waterfront from an open helicopter door"/>
    <path d="M520 20H805A75 75 0 0 1 805 170H520C510 120 510 70 520 20Z" fill="var(--ink)"/>
    <rect x="455" y="289" width="250" height="3" fill="#d7d9de"/>
  </svg>
  <div class="headline" style="left:530px;top:28px;font-size:66px;color:var(--white)">See Tampa<br>From Above</div>
  <div class="offer" style="left:530px;top:198px;font-size:25px;color:var(--blue);line-height:1.3">Take <b style="font-size:44px">$25</b>Off<br>with Code <b style="font-size:44px">UP25</b></div>
  <div class="brand" style="left:870px;top:185px"><i></i>SkyMarlo</div>
  <div class="site blue" style="left:802px;top:240px;width:268px"><svg><use href="#globe"/></svg>www.skyMARLO.com</div>
</div>

<!-- Elevate -->
<div class="board" style="top:1516px">
  <svg class="shapes" viewBox="0 0 1070 309">
    <path d="M340 309C360 250 420 230 500 240V309Z" fill="var(--ink)"/>
    <path d="M760 0H830C820 30 800 50 780 60Z" fill="var(--blue)"/>
    <ellipse cx="590" cy="160" rx="262" ry="160" fill="var(--white)"/>
    <ellipse cx="590" cy="160" rx="252" ry="157" fill="url(#dusk)" role="img" aria-label="Feet dangling over Tampa bay and skyline at sunset"/>
    <path d="M910 22H1070V150H910A64 64 0 0 1 910 22Z" fill="var(--blue)"/>
    <path d="M0 251H285A17 17 0 0 1 285 285H0Z" fill="var(--ink)"/>
  </svg>
  <div class="headline" style="left:32px;top:30px;width:272px;text-align:center;font-size:66px;line-height:.97">Elevate<br>Your<br>Weekend</div>
  <div class="offer" style="left:858px;top:30px;width:212px;text-align:center;font-size:22px;line-height:1.15">Use Code<br><b style="font-size:36px">YES25</b> for<br><b style="font-size:36px">$25</b> Off</div>
  <div class="brand" style="left:885px;top:228px"><i></i>SkyMarlo</div>
  <div class="site" style="left:30px;top:251px;background:transparent"><svg><use href="#globe"/></svg>www.skyMARLO.com</div>
</div>

<!-- Premium Views -->
<div class="board" style="top:1885px">
  <svg class="shapes" viewBox="0 0 1070 309">
    <rect x="400" y="22" width="670" height="10" fill="#d9dbe0"/>
    <path d="M0 0H340C420 30 440 120 400 180C470 140 540 200 545 309H0Z" fill="var(--blue)"/>
    <path d="M0 0H330C410 40 420 130 380 190C450 160 520 210 530 309H0Z" fill="url(#beach)" role="img" aria-label="Red helicopter flying along St. Pete beach shoreline"/>
    <path d="M400 34H1070V108H390C395 80 400 60 400 34Z" fill="var(--ink)"/>
    <path d="M390 108H990A32 32 0 0 1 990 172H390Z" fill="var(--blue)"/>
    <path d="M390 134H488A10 10 0 0 1 488 154H390Z" fill="#3f8cf5"/>
    <path d="M785 250H1070V284H785A17 17 0 0 1 785 250Z" fill="var(--ink)"/>
  </svg>
  <div class="headline" style="left:410px;top:38px;font-size:62px;color:var(--white)">Premium Views. No Filter</div>
  <div class="offer" style="left:515px;top:117px;font-size:22px">Take <b style="font-size:38px">$25</b> Off with Code <b style="font-size:38px">SKY25</b></div>
  <div class="brand" style="left:590px;top:225px"><i></i>SkyMarlo</div>
  <div class="site" style="left:785px;top:250px;background:transparent"><svg><use href="#globe"/></svg>www.skyMARLO.com</div>
</div>

<!-- Sunset -->
<div class="board" style="top:2254px">
  <svg class="shapes" viewBox="0 0 1070 309">
    <path d="M470 0H1070V309H520C460 220 440 90 470 0Z" fill="var(--ink)"/>
    <path d="M490 0H1070V309H540C480 220 460 90 490 0Z" fill="url(#sunset)" role="img" aria-label="Blue helicopter over Tampa skyline at sunset"/>
    <circle cx="1020" cy="275" r="65" fill="var(--blue)"/>
    <path d="M330 178C350 128 400 112 480 112H580V222H330Z" fill="var(--blue)"/>
    <path d="M330 267A17 17 0 0 1 347 250H600V284H347A17 17 0 0 1 330 267Z" fill="var(--ink)"/>
  </svg>
  <div class="headline" style="left:34px;top:28px;font-size:66px;line-height:.95">Sunset Hits<br>Different</div>
  <div class="offer" style="left:355px;top:117px;width:180px;text-align:center;font-size:20px;line-height:1.15">Use Code<br><b style="font-size:34px">SUNSET25</b><br>for <b style="font-size:34px">$25</b> Off</div>
  <div class="brand" style="left:34px;top:228px"><i></i>SkyMarlo</div>
  <div class="site" style="left:330px;top:250px;background:transparent"><svg><use href="#globe"/></svg>www.skyMARLO.com</div>
</div>

</body>
</html>
```